Slim Can Designs! Single Origin Coffee Cold Brew Coffee Cans

Amber Heron is a lifestyle brand with a focus on producing coffee. We need a three labels designed for our Cold Brew Cans. These will be 12 oz. slim cans for cold brew coffee. Each can will represent a different flavor profile tied to a virtue. Template Attached. We only have three products for cold brew cans. Please also review all the files included in our project for reference.
1. Gratitude : Toffee, Smokey, Chocolate
Things to include: Single Origin Coffee Dark Roast / Bold and Strong
2. Patience : Caramel, Chocolate, Dried Mango / Bright and Sparkling
Things to include: Single Origin Coffee Medium Roast
3. Kindness : Berry, Citrus, Floral / Smooth and Rich
Things to include: Single Origin Coffee Light Roast
All cans should include:
1. our logo. and brand colors.
2. all virtue icons if possible ?
3. Nutrition Label attached. Use this for all three, it may change but please use for placeholder.
4. Barcode
5. Net wt. 12oz
6. Ingredients : Single Origin Coffee, Water
7. BE KIND DRINK COFFEE
8. EST 2007
9. Roasted in Portland
10. Our business name and address:
Amber Heron Coffee Roasters
Portland, Oregon
web amberheronco.com
instagram amberheronco
11. Ethically Sourced Coffee Icon: if you can create one
12. Please recycle icon
13. Shake Lightly and Serve Chilled
14. Caffeine Content 200mg. : this might change between product but please use this as a placeholder for now.
15.

These designs should be cohesive and have some connection to our other brand element to tie together with our other current product designs. We are looking for sleek but fun and bold with colors and elements.

Target Market(s)

Mass market

Industry/Entity Type

Coffee

Font styles to use
Sans Serif
Other font styles liked:
• Please refer to our brand kit

Requirements
Must have
• Please refer to description
Nice to have

```html
<!DOCTYPE html>
<html lang="en">
<head>
<meta charset="utf-8">
<title>Amber Heron Cold Brew Can Labels</title>
<link href="https://fonts.googleapis.com/css2?family=Oswald:wght@700&family=Montserrat:wght@400;500;600;700&family=Lobster&display=swap" rel="stylesheet">
<style>
  :root{
    --bg:#e6e6e6;
    --navy:#1f3a5c;
    --gold:#d8b689;
    --teal:#4f8d80;
    --teal-dark:#3f7a6e;
    --berry:#b63b57;
    --silver-1:#c9cbd0;
    --silver-2:#f7f7f8;
    --white:#ffffff;
  }
  *{box-sizing:border-box;margin:0;padding:0}
  html,body{width:1200px;height:1097px;overflow:hidden}
  body{
    background:linear-gradient(180deg,#ffffff 0%,var(--bg) 100%);
    font-family:"Montserrat",sans-serif;
    position:relative;
  }
  .can{
    position:absolute;top:228px;width:240px;height:640px;
    border-radius:14px;overflow:hidden;
    display:flex;flex-direction:column;
    box-shadow:0 18px 30px rgba(0,0,0,.12);
  }
  .can--patience{left:130px;--top:var(--gold);--stripe:var(--navy);--mid:var(--navy);--pill:var(--gold);--pill-ink:var(--navy);--accent:var(--gold);--name:var(--navy)}
  .can--gratitude{left:480px;--top:var(--navy);--stripe:var(--teal);--mid:var(--teal);--pill:var(--navy);--pill-ink:var(--white);--accent:var(--teal-dark);--name:var(--navy)}
  .can--kindness{left:830px;--top:var(--berry);--stripe:var(--navy);--mid:var(--navy);--pill:var(--berry);--pill-ink:var(--white);--accent:var(--berry);--name:var(--berry)}

  .band{background:var(--top);flex:0 0 auto}
  .band--top{height:68px}
  .band--bottom{height:60px;display:flex;align-items:center;justify-content:center;
    color:var(--white);font-size:9px;font-weight:700}
  .stripe{height:8px;background:var(--stripe)}

  .label{
    height:324px;flex:0 0 auto;
    background:linear-gradient(90deg,var(--silver-1) 0%,var(--silver-2) 45%,var(--white) 55%,var(--silver-1) 100%);
    display:flex;flex-direction:column;align-items:center;padding-top:22px;
  }
  .brand{display:flex;flex-direction:column;align-items:center;color:var(--navy)}
  .brand__dot{width:30px;height:30px;border-radius:50%;background:var(--navy);margin-bottom:8px}
  .brand__name{font-size:12.5px;font-weight:500;line-height:1.05;text-align:center;letter-spacing:.2px}
  .brand__tag{font-size:6px;letter-spacing:1.6px;margin-top:2px}
  .est{display:flex;align-items:center;gap:4px;margin-top:12px}
  .est__line{width:38px;height:2px;background:var(--accent)}
  .est__pill{background:var(--accent);color:var(--white);font-size:6.5px;font-weight:600;
    padding:2px 6px;border-radius:6px}
  .virtue{font-family:"Oswald",sans-serif;font-weight:700;color:var(--name);
    font-size:48px;line-height:1;margin-top:14px;letter-spacing:-.5px}
  .notes{display:flex;align-items:center;gap:10px;margin-top:14px}
  .notes__icon{width:40px;height:40px;border-radius:50%;background:var(--accent)}
  .notes__list{list-style:none;color:var(--navy);font-size:12px;font-weight:500;line-height:1.25}

  .panel{flex:1 1 auto;background:var(--mid);display:flex;flex-direction:column;align-items:center;padding-top:18px}
  .script{font-family:"Lobster",cursive;color:var(--white);font-size:22px;line-height:.9;text-align:center;
    transform:rotate(-4deg)}
  .roast{margin-top:18px;background:var(--pill);color:var(--pill-ink);font-weight:700;
    font-size:12.5px;padding:4px 16px;border-radius:10px;letter-spacing:.3px}
  .origin{display:flex;align-items:center;gap:10px;margin-top:12px;color:var(--white)}
  .origin__badge{width:28px;height:28px;border-radius:50%;border:1.5px solid var(--white);opacity:.8}
  .origin__text{font-size:10px;font-weight:600;line-height:1.35}
</style>
</head>
<body>

<section class="can can--patience">
  <div class="band band--top" role="img" aria-label="Gold band with a faint coffee leaf and bean pattern"></div>
  <div class="stripe"></div>
  <div class="label">
    <div class="brand">
      <span class="brand__dot"></span>
      <span class="brand__name">AMBER HERON<br>COFFEE ROASTERS</span>
      <span class="brand__tag">SINGLE ORIGIN COFFEE</span>
    </div>
    <div class="est"><span class="est__line"></span><span class="est__pill">EST 2007</span><span class="est__line"></span></div>
    <h2 class="virtue">PATIENCE</h2>
    <div class="notes">
      <span class="notes__icon" role="img" aria-label="Patience virtue icon"></span>
      <ul class="notes__list"><li>CARAMEL</li><li>CHOCOLATE</li><li>DRIED MANGO</li></ul>
    </div>
  </div>
  <div class="panel">
    <p class="script">Single Origin<br>Coffee</p>
    <p class="roast">MEDIUM ROAST</p>
    <div class="origin"><span class="origin__badge"></span><p class="origin__text">Roasted in<br>Portland</p></div>
  </div>
  <div class="band band--bottom" role="img" aria-label="Gold band with a faint coffee leaf and bean pattern"><span style="color:var(--navy)">Net Weight: 12 oz.</span></div>
</section>

<section class="can can--gratitude">
  <div class="band band--top" role="img" aria-label="Navy band with a faint coffee leaf and bean pattern"></div>
  <div class="stripe"></div>
  <div class="label">
    <div class="brand">
      <span class="brand__dot"></span>
      <span class="brand__name">AMBER HERON<br>COFFEE ROASTERS</span>
      <span class="brand__tag">SINGLE ORIGIN COFFEE</span>
    </div>
    <div class="est"><span class="est__line"></span><span class="est__pill">EST 2007</span><span class="est__line"></span></div>
    <h2 class="virtue">GRATITUDE</h2>
    <div class="notes">
      <span class="notes__icon" role="img" aria-label="Gratitude virtue icon"></span>
      <ul class="notes__list"><li>TOFFEE</li><li>SMOKEY</li><li>CHOCOLATE</li></ul>
    </div>
  </div>
  <div class="panel">
    <p class="script">Single Origin<br>Coffee</p>
    <p class="roast">BOLD AND STRONG</p>
    <div class="origin"><span class="origin__badge"></span><p class="origin__text">Roasted in<br>Portland</p></div>
  </div>
  <div class="band band--bottom" role="img" aria-label="Navy band with a faint coffee leaf and bean pattern">Net Weight: 12 oz.</div>
</section>

<section class="can can--kindness">
  <div class="band band--top" role="img" aria-label="Berry band with a faint coffee leaf and bean pattern"></div>
  <div class="stripe"></div>
  <div class="label">
    <div class="brand">
      <span class="brand__dot"></span>
      <span class="brand__name">AMBER HERON<br>COFFEE ROASTERS</span>
      <span class="brand__tag">SINGLE ORIGIN COFFEE</span>
    </div>
    <div class="est"><span class="est__line"></span><span class="est__pill">EST 2007</span><span class="est__line"></span></div>
    <h2 class="virtue">KINDNESS</h2>
    <div class="notes">
      <span class="notes__icon" role="img" aria-label="Kindness virtue icon"></span>
      <ul class="notes__list"><li>BERRY</li><li>CITRUS</li><li>FLORAL</li></ul>
    </div>
  </div>
  <div class="panel">
    <p class="script">Single Origin<br>Coffee</p>
    <p class="roast">LIGHT ROAST</p>
    <div class="origin"><span class="origin__badge"></span><p class="origin__text">Roasted in<br>Portland</p></div>
  </div>
  <div class="band band--bottom" role="img" aria-label="Berry band with a faint coffee leaf and bean pattern">Net Weight: 12 oz.</div>
</section>

</body>
</html>
```